Harold Penwick Sausage Label Design

Talmore Fields Corporation is seeking to create a new brand of fresh 100% Canadian pork sausage. This label will be a paper band that slips on and off foam trays. The front facing side will be 5 inches wide by 3.5 inches high. The following is some information about our brand.
Target market:
1. Working Moms
2. Stay at home moms
3. Barbeque enthusiast
Brand personality
1. Old school values – We are a family run company who believes in an honest days work
2. Modern day sensibility – We believe in being nimble and open to new ideas
3. Energetic and optimistic – We are passionate about our business and product
4. Relaxed sense of humor – We believe that it is possible to work hard and have fun
Positioning Statements:
Our sausage is the easy choice for adding flavour to your real- life family meals, that’s because:
1. It is 100% fresh Canadian product with no fillers or preservatives
2. It is a great tasting recipe with simple, natural ingredients
3. It is brought to you with good humor and integrity by a multi- generational family owned business
We are looking for a creative designer to make our ideas come to life. There are three types of designs we would like to see:
1. Rustic – a rustic, barbequing, old farm, country feel – without feeling too old
2. Modern & Simple – Very simple clean face with clean text
3. Family friendly – a label that would appeal to the everyday family with photos of the finished product
This brand does not have a name yet, please use the name “Harold Penwick “as a place holder. Please keep in mind the information provided about our brand when developing the label. Attached are pictures of some ideas we like. Please do not copy these ideas too closely, we are looking to differentiate ourselves in the market. Samples are to provide some guidance of our preferences.
Target Market(s)
1. Working Moms
2. Stay at home moms
3. Barbeque enthusiast
Colors
Designer to choose colors to be used in the design.
Look and feel
Each slider illustrates characteristics of the customer's brand and the style your logo design should communicate.

```html
<!DOCTYPE html>
<html lang="en">
<head>
<meta charset="utf-8">
<title>Harold Penwick – Mutton &amp; Mint Sausage Label</title>
<link rel="stylesheet" href="https://fonts.googleapis.com/css2?family=Alfa+Slab+One&family=Arvo:wght@700&family=Yellowtail&display=block">
<style>
  :root {
    --label-red: #cd3d47;
    --cream: #efeedc;
    --ink: #2b1719;
    --slab-heavy: "Alfa Slab One", serif;
    --slab: "Arvo", serif;
    --script: "Yellowtail", cursive;
  }
  html, body { margin: 0; padding: 0; overflow: hidden; }
  .label {
    position: relative;
    width: 1200px;
    height: 843px;
    background: var(--label-red);
    overflow: hidden;
    color: var(--cream);
  }
  .label p, .label h1, .label h2 { z-index: 2; }
  .rule { position: absolute; background: var(--cream); }
  .rule--h { height: 3px; }
  .rule--v { width: 3px; }

  .maker {
    position: absolute; left: 50px; top: 72px; margin: 0;
    font: 700 23px/1 var(--slab); letter-spacing: 0.5px;
  }
  .brand {
    position: absolute; left: 40px; top: 168px; margin: 0;
    font: 400 76px/1.32 var(--slab-heavy);
    text-shadow: 5px 5px 0 var(--ink);
    text-transform: uppercase;
    white-space: nowrap;
  }
  .brand span { display: block; }

  .hero-art {
    position: absolute; left: 590px; top: 80px; width: 520px; height: 368px;
  }
  .origin-map {
    position: absolute; left: 64px; top: 530px; width: 172px; height: 140px;
    z-index: 1;
  }
  .origin-claim {
    position: absolute; left: 250px; top: 480px; margin: 0;
    font: 400 30px/0.95 var(--script);
    transform: rotate(-4deg);
    white-space: nowrap;
  }
  .natural {
    position: absolute; left: 428px; top: 478px; margin: 0;
    font: 400 40px/1 var(--script);
    white-space: nowrap;
  }
  .flavour {
    position: absolute; left: 430px; top: 564px; margin: 0;
    font: 400 54px/1 var(--slab-heavy); color: var(--ink);
    letter-spacing: 0.5px;
    white-space: nowrap;
  }
  .product-type {
    position: absolute; left: 440px; top: 630px; margin: 0;
    font: 700 30px/1 var(--slab);
  }
  .count {
    position: absolute; left: 70px; top: 722px; margin: 0;
    font: 700 30px/1 var(--slab);
  }
  .weight {
    position: absolute; left: 194px; top: 716px; margin: 0;
    font: 700 30px/1 var(--slab);
    display: flex; align-items: center; gap: 12px;
  }
  .weight svg { display: block; }
  .storage {
    position: absolute; left: 194px; top: 757px; margin: 0;
    font: 700 14.5px/1 var(--slab);
    white-space: nowrap;
  }
  .description {
    position: absolute; left: 440px; top: 712px; margin: 0;
    font: 700 30px/1.3 var(--slab);
    white-space: nowrap;
  }
</style>
</head>
<body>
<main class="label">
  <div class="rule rule--v" style="left:507px;top:50px;height:410px"></div>
  <div class="rule rule--h" style="left:46px;top:125px;width:461px"></div>
  <div class="rule rule--h" style="left:44px;top:459px;width:1110px"></div>
  <div class="rule rule--v" style="left:407px;top:459px;height:338px"></div>
  <div class="rule rule--h" style="left:407px;top:543px;width:747px"></div>
  <div class="rule rule--h" style="left:44px;top:689px;width:1110px"></div>
  <div class="rule rule--v" style="left:161px;top:689px;height:108px"></div>

  <p class="maker">TALMORE FIELDS CORPORATION</p>
  <h1 class="brand"><span>Harold</span><span>Penwick</span></h1>

  <svg class="hero-art" role="img" aria-label="Illustration of a grilled sausage on a fork" viewBox="0 0 520 368">
    <defs>
      <linearGradient id="heroTone" x1="0" y1="0" x2="0" y2="1">
        <stop offset="0" stop-color="#efeedc"/>
        <stop offset="1" stop-color="#2b1719"/>
      </linearGradient>
    </defs>
    <rect width="520" height="368" rx="28" fill="url(#heroTone)" opacity="0.35"/>
  </svg>

  <svg class="origin-map" role="img" aria-label="Map of Canada" viewBox="0 0 172 140">
    <rect width="172" height="140" rx="16" fill="#efeedc"/>
  </svg>
  <p class="origin-claim">100%<br>Canadian</p>

  <p class="natural">All Natural</p>
  <h2 class="flavour">MUTTON &amp; MINT</h2>
  <p class="product-type">PORK SAUSAGES</p>

  <p class="count">X6</p>
  <p class="weight">400G
    <svg width="38" height="30" viewBox="0 0 38 30" aria-label="estimated sign">
      <path d="M3 15 H35 A16 13 0 1 0 30 25" fill="none" stroke="#efeedc" stroke-width="3"/>
    </svg>
  </p>
  <p class="storage">KEEP REFRIGERATED</p>

  <p class="description">6 MATURE MUTTON&nbsp; SAUSAGE,<br>INFUSED WITH MINT.</p>
</main>
</body>
</html>
```